One Pager Fact Sheet Design

I need a couple of headers and footer designed to use for information security fact sheets to give to customers. Similar to the one listed below.

```html
<!DOCTYPE html>
<html lang="en">
<head>
<meta charset="utf-8">
<title>Nexaline Communications – Fact Sheet Headers and Footer</title>
<link rel="stylesheet" href="https://fonts.googleapis.com/css2?family=Source+Sans+3:wght@400;700;800&display=swap">
<style>
  :root {
    --red-bright: #f41414;
    --red-mid: #d80c0c;
    --red-deep: #ad0606;
    --white: #ffffff;
    --paper: #f7f7f7;
    --ink: #1e1e1e;
    --accent-red: #e3121b;
    --social-blue: #1b8fd2;
    --art-orange: #f07a3a;
    --art-blue: #3fa8e0;
  }
  * { box-sizing: border-box; margin: 0; padding: 0; }
  html, body {
    width: 1200px; height: 796px; overflow: hidden;
    background: var(--white);
    font-family: "Source Sans 3", Arial, sans-serif;
  }
  .sheet { position: relative; width: 1200px; height: 796px; }

  .banner {
    position: absolute; left: 126px; width: 949px; overflow: hidden;
    box-shadow: 0 6px 10px rgba(0,0,0,0.35);
  }
  .banner__bg { position: absolute; inset: 0; width: 100%; height: 100%; }

  .header--main { top: 169px; height: 165px; background: linear-gradient(90deg, var(--red-bright) 0%, var(--red-mid) 55%, var(--red-deep) 100%); }
  .header--compact { top: 374px; height: 110px; background: linear-gradient(90deg, var(--red-deep) 0%, var(--red-mid) 50%, var(--red-bright) 100%); }

  .brand { position: absolute; display: flex; align-items: center; color: var(--white); }
  .brand__mark { border: 4px solid var(--white); border-radius: 50%; flex: none; }
  .brand__text { font-weight: 800; line-height: 0.9; letter-spacing: -0.5px; }
  .brand__tagline { display: block; font-size: 12px; letter-spacing: 3.6px; text-align: right; margin-top: 2px; }

  .header--main .brand { left: 38px; top: 56px; gap: 10px; }
  .header--main .brand__mark { width: 48px; height: 48px; }
  .header--main .brand__text { font-size: 40px; }

  .header--compact .brand { left: 46px; top: 38px; gap: 8px; }
  .header--compact .brand__mark { width: 34px; height: 34px; border-width: 3px; }
  .header--compact .brand__text { font-size: 18px; }

  .security-art {
    position: absolute; border-radius: 6px;
    background: linear-gradient(90deg, var(--art-blue) 0%, var(--art-orange) 35%, #c9c9c9 70%, #8f1a1a 100%);
    opacity: 0.85;
  }
  .header--main .security-art { left: 572px; top: 43px; width: 342px; height: 80px; }
  .header--compact .security-art { left: 566px; top: 18px; width: 354px; height: 80px; }

  .footer { top: 542px; height: 88px; background: var(--paper); }
  .contact {
    position: absolute; top: 32px; display: flex; align-items: center; gap: 6px;
    font-size: 17px; color: var(--ink); white-space: nowrap; line-height: 1;
  }
  .contact__icon { width: 22px; height: 22px; flex: none; }
  .contact--web { left: 33px; }
  .contact--profile { left: 304px; }
  .contact--phone { left: 643px; }
  .footer__divider { position: absolute; left: 796px; top: 28px; width: 3px; height: 34px; background: var(--accent-red); }
  .social { position: absolute; left: 814px; top: 33px; display: flex; gap: 8px; list-style: none; }
  .social__item { width: 23px; height: 23px; border-radius: 50%; background: var(--social-blue); }
</style>
</head>
<body>
<main class="sheet">

  <section class="banner header--main" aria-label="Main header">
    <svg class="banner__bg" viewBox="0 0 949 165" preserveAspectRatio="none" aria-hidden="true">
      <polygon points="0,0 180,0 0,120" fill="#ff3a3a" opacity="0.35"/>
      <polygon points="120,0 560,0 380,165 0,165 0,110" fill="#ffffff" opacity="0.06"/>
      <polygon points="300,165 560,0 600,0 360,165" fill="#7a0000" opacity="0.18"/>
      <polygon points="0,165 200,40 260,165" fill="#7a0000" opacity="0.12"/>
    </svg>
    <div class="brand">
      <span class="brand__mark"></span>
      <span class="brand__text">nexaline<span class="brand__tagline">communications</span></span>
    </div>
    <div class="security-art" role="img" aria-label="Illustration of information security icons: cloud lock, globe, email shield, documents, servers, padlock, phone and laptop with shield"></div>
  </section>

  <section class="banner header--compact" aria-label="Compact header">
    <svg class="banner__bg" viewBox="0 0 949 110" preserveAspectRatio="none" aria-hidden="true">
      <polygon points="680,110 860,0 949,0 949,110" fill="#ff2a2a" opacity="0.35"/>
      <polygon points="560,110 740,0 800,0 640,110" fill="#7a0000" opacity="0.15"/>
      <polygon points="0,0 200,0 0,90" fill="#7a0000" opacity="0.12"/>
    </svg>
    <div class="brand">
      <span class="brand__mark"></span>
      <span class="brand__text">nexaline</span>
    </div>
    <div class="security-art" role="img" aria-label="Illustration of information security icons: cloud lock, globe, email shield, documents, servers, padlock, phone and laptop with shield"></div>
  </section>

  <footer class="banner footer" aria-label="Contact footer">
    <div class="contact contact--web">
      <svg class="contact__icon" viewBox="0 0 22 22" aria-hidden="true">
        <circle cx="11" cy="11" r="11" fill="var(--accent-red)"/>
        <g fill="none" stroke="#fff" stroke-width="1.3">
          <circle cx="11" cy="11" r="6"/><ellipse cx="11" cy="11" rx="2.6" ry="6"/><line x1="5" y1="11" x2="17" y2="11"/>
        </g>
      </svg>
      <span>nexaline.in&nbsp; nexaline.net.org</span>
    </div>
    <div class="contact contact--profile">
      <svg class="contact__icon" viewBox="0 0 22 22" aria-hidden="true">
        <circle cx="11" cy="11" r="11" fill="var(--accent-red)"/>
        <polygon points="6,6 16,10 11.5,11.5 10,16" fill="#fff"/>
      </svg>
      <span>network.com/company/nexaline.net.org</span>
    </div>
    <div class="contact contact--phone">
      <svg class="contact__icon" viewBox="0 0 22 22" aria-hidden="true">
        <circle cx="11" cy="11" r="11" fill="var(--accent-red)"/>
        <path d="M5 9c0-2 3-3 6-3s6 1 6 3v1h-3V8.5h-6V10H5z" fill="#fff"/>
        <rect x="6.5" y="11" width="9" height="5" rx="1" fill="#fff"/>
      </svg>
      <span>01632 960 482</span>
    </div>
    <span class="footer__divider" aria-hidden="true"></span>
    <ul class="social" aria-label="Social profiles">
      <li class="social__item"></li>
      <li class="social__item"></li>
      <li class="social__item"></li>
      <li class="social__item"></li>
    </ul>
  </footer>

</main>
</body>
</html>
```